Tolvik service sheets and folder

A set of 12 Service sheets plus a rate card to be inserted into a folder - each to be designed and formatted.
A4
Portrait
- the idea is to keep things simple and crisp.
I would use the logo (see attached .ai file) at the top and maybe an separate image to go with each sheet

Around 350 words per page (see attached example)
The format is mainly text and bullet points, but each page will be same layout (just a different image as indicated above).

Need to factor in a folder to hold the service sheets.

The documents to have a good sales impact and your experience and advice on best ideas would be welcome. The key is to keep it crisp, elegant & professional for financial services.

The output files should be in PDF and raw file formats so that printing can be managed easily in future., Details for my new Catalogue Design Project will be added soon.

Industry/Entity Type

Financial

Requirements
Must have
• Inspire us!
Should not have
• No images of people or parts (like hands, arms) etc

```html
<!DOCTYPE html>
<html lang="en">
<head>
<meta charset="utf-8">
<title>Tolvik – Investment Management Service Sheet</title>
<link rel="stylesheet" href="https://fonts.googleapis.com/css2?family=Istok+Web:wght@400;700&display=swap">
<style>
  :root {
    --ink: #3a3a3a;
    --ink-soft: #4a4a4a;
    --band-deep: #0a2f4f;
    --band-mid: #1b6a93;
    --band-light: #bfe6f5;
    --brand: #2a2a2a;
    --brand-dot: #b3123a;
    --paper: #ffffff;
  }
  * { margin: 0; padding: 0; box-sizing: border-box; }
  html, body { width: 848px; height: 1200px; overflow: hidden; background: var(--paper); }
  body {
    position: relative;
    font-family: "Istok Web", "Helvetica Neue", Arial, sans-serif;
    color: var(--ink);
  }
  .band {
    position: absolute;
    left: 80px;
    width: 688px;
    background:
      radial-gradient(ellipse 120px 30px at 62% 55%, rgba(191,230,245,.75), transparent 70%),
      radial-gradient(ellipse 160px 40px at 30% 40%, rgba(70,150,190,.5), transparent 70%),
      linear-gradient(90deg, var(--band-deep), var(--band-mid) 45%, #2f88b2 62%, var(--band-mid) 78%, var(--band-deep));
  }
  .band--top { top: 0; height: 26px; }
  .band--bottom { top: 1157px; height: 43px; }

  .block { position: absolute; left: 82px; width: 690px; }
  .intro { top: 131px; font-size: 13.2px; line-height: 21.6px; }
  h2 {
    font-size: 13.8px;
    font-weight: 700;
    color: var(--ink-soft);
    letter-spacing: .2px;
    margin-bottom: 5px;
  }
  ul { list-style: none; font-size: 13.2px; line-height: 21.6px; }
  li { position: relative; padding-left: 20px; }
  li::before {
    content: "";
    position: absolute;
    left: 2px; top: 8px;
    width: 5px; height: 5px;
    border-radius: 50%;
    background: var(--ink);
  }
  .key-features { top: 260px; }
  .risks { top: 413px; }
  .additional { top: 522px; }
  .associated { top: 696px; }

  .brand {
    position: absolute; left: 84px; top: 840px;
    display: flex; align-items: center; gap: 12px;
  }
  .brand__dot { width: 44px; height: 44px; border-radius: 50%; background: var(--brand-dot); }
  .brand__name { font-size: 28px; font-weight: 400; color: var(--brand); letter-spacing: 1px; }

  .contact { top: 910px; font-size: 13.2px; line-height: 21.6px; }

  .disclaimer { top: 979px; width: 684px; font-size: 9.3px; line-height: 13.6px; color: var(--ink); }
  .disclaimer strong { font-weight: 700; }
</style>
</head>
<body>
  <div class="band band--top" role="img" aria-label="Blue water texture band"></div>

  <p class="block intro">Our role is to assist investors acquire a stake in the world economy through diversified portfolios. Investment processes blend our strategic view, a tactical overlay, an asset allocation policy and research of individual investment opportunities on a long term basis. We do not confine ourselves to a particular methodology, but we look for value, using such traditional measures as yield, price to book and the discounted value of cash flows. We aim to invest in companies that grow their dividends in the belief that an increasing income supports capital values.</p>

  <section class="block key-features">
    <h2>Key Features:</h2>
    <ul>
      <li>A fully tailored investment management service with access to a personal investment manager.</li>
      <li>Each portfolio fully tailored to fulfil your individual requirements and monitored to ensure lifestyle<br>changes are duly considered.</li>
      <li>A flexible product including access to investment expertise in smaller companies and derivatives if desired.</li>
      <li>Independent and unbiased advice.</li>
    </ul>
  </section>

  <section class="block risks">
    <h2>Risks</h2>
    <ul>
      <li>The value of your investments and any income from them may go down and you may get back<br>less than you invested.</li>
      <li>If you are unsure about the suitability of the products please contact us for advice.</li>
    </ul>
  </section>

  <section class="block additional">
    <h2>Additional Features:</h2>
    <ul>
      <li>Minimum portfolio size of GBP100,000.</li>
      <li>On-line access to review holdings.</li>
      <li>Regular portfolio valuations provided.</li>
      <li>Nominee service for custody of assets globally.</li>
      <li>Investment income transferred to an interest bearing account.</li>
      <li>Derivatives can be used as part of a hedging or covered income enhancement strategy, where required.</li>
    </ul>
  </section>

  <section class="block associated">
    <h2>Associated Services:</h2>
    <ul>
      <li>ISAs: Managed and Self Select.</li>
      <li>Managed Funds Service</li>
      <li>Independent SIPP Investment Management</li>
      <li>Advisory Dealing</li>
    </ul>
  </section>

  <div class="brand">
    <span class="brand__dot"></span>
    <span class="brand__name">TOLVIK</span>
  </div>

  <p class="block contact">For a confidential discussion<br>please contact us on: +44 (0)20 7946 0123&nbsp; or via our website www.tolvik.com.</p>

  <div class="block disclaimer">
    <p><strong>Disclaimer:</strong></p>
    <p>Tolvik operates as a division of Harrowgate Capital Plc (Harrowgate) under a Trade Name Services Agreement. Harrowgate is a member of the Northgate Stock Exchange and is authorised and regulated by the Financial Standards Authority. Registered in England and Wales number 04817263. Registered Office 14-18 Elmfield Row London NW3 7XL.</p>
    <p>This communication and all information contained in or attached to it (including, but not limited to market prices/levels and market commentary) (the "Information") is for informational purposes only, is confidential, may be legally privileged and is the intellectual property of Tolvik. The Information is not, and should not be construed as, an offer, bid, recommendation or solicitation in relation to any financial instrument or investment or to participate in any particular trading strategy. The Information is not to be relied upon and is not warranted, including, but not limited, as to completeness, timeliness or accuracy and is subject to change without notice. All representations and warranties are expressly disclaimed. Access to the Information by anyone other than the intended recipient is unauthorised and any disclosure, copying or redistribution is prohibited. For further regulatory information and our terms of business, please see <strong>www.tolvik.com and www.harrowgategroup.com.</strong> If you receive this communication in error, please safely dispose of all copies of it in a timely manner and notify us (by e-mail to clientservices@tolvik.com or by telephone on +44 (0)20 7946 0123).</p>
  </div>

  <div class="band band--bottom" role="img" aria-label="Blue water texture band"></div>
</body>
</html>
```